Bref créative
Business Card for Business Advisory Firm
Marlowe Partners
Simple
Tom Brackett
Solutions Strategist
47 Pellham Road
Suite K
Boston, MA 02184
tbrackett@marlowepartners.example
www.marlowepartners.example
Somewhere on the front of the card I would like to list some of the services of the firm:
Project Support
Operations Analysis
Business Development
Would like a blue gingham pattern on entire back using the same colors as in the logo.
Layout guidelines: I will be using Zeb to print the cards. If there are any questions about layout for bleed etc, they can be found at link below:
http://us.zebprint.example/help/faq/templates-and-guidelines.html
Final, trimmed size
3.30" x 2.16"
84mm x 55mm
Full bleed size (recommended for creating finished artwork)
1039 x 697 pixels (300dpi)
3.46" x 2.32" (300dpi)
88mm x 59mm (300dpi)

```html
<!DOCTYPE html>
<html lang="en">
<head>
<meta charset="utf-8">
<title>Marlowe Partners – Business Card</title>
<link rel="stylesheet" href="https://fonts.googleapis.com/css2?family=Open+Sans:ital,wght@0,400;0,600;0,700;0,800;1,400&display=swap">
<style>
  :root {
    --brand-blue: #2b35b8;
    --brand-blue-dark: #1f2896;
    --brand-blue-light: #4b63d6;
    --paper: #fbfbfb;
    --ink-grey: #6b6f7a;
    --backdrop: #dcdcde;
  }
  * { box-sizing: border-box; margin: 0; padding: 0; }
  html, body {
    width: 1200px; height: 904px; overflow: hidden;
    background: var(--backdrop);
    font-family: "Open Sans", Arial, sans-serif;
  }
  .card-sheet {
    position: relative; width: 1200px; height: 904px;
  }
  .card {
    position: absolute; top: 275px;
    width: 540px; height: 354px;
    box-shadow: 0 6px 18px rgba(0,0,0,0.18);
    overflow: hidden;
  }
  /* Front */
  .card--front { left: 40px; background: var(--paper); }
  .brand-lockup {
    position: absolute; left: 62px; top: 48px;
    display: flex; align-items: flex-start; gap: 14px;
  }
  .brand-square {
    width: 58px; height: 58px; background: var(--brand-blue); margin-top: 4px;
  }
  .brand-name {
    color: var(--brand-blue); font-weight: 800; line-height: 0.95;
  }
  .brand-name__first { display: block; font-size: 50px; letter-spacing: -1px; }
  .brand-name__second { display: block; font-size: 32px; text-align: right; letter-spacing: -0.5px; }
  .service-list {
    position: absolute; left: 120px; top: 150px;
    list-style: none; color: var(--ink-grey);
    font-size: 12px; line-height: 1.35; text-align: right; width: 170px;
  }
  .contact-person {
    position: absolute; left: 62px; top: 214px;
    color: var(--ink-grey); font-size: 12px; line-height: 1.4;
  }
  .contact-person__name { color: var(--brand-blue); font-weight: 700; font-size: 15px; }
  .contact-person__title { color: var(--brand-blue); margin-bottom: 4px; }
  .contact-lines {
    position: absolute; left: 300px; top: 186px;
    list-style: none; color: var(--ink-grey); font-size: 12px;
  }
  .contact-lines li { display: flex; align-items: center; gap: 8px; height: 19px; }
  .contact-icon { width: 13px; height: 13px; flex: none; }
  .front-band { position: absolute; left: 0; bottom: 0; width: 540px; height: 40px; }

  /* Back */
  .card--back { left: 620px; background: var(--brand-blue); }
  .back-lockup {
    position: absolute; left: 0; right: 0; top: 120px;
    display: flex; justify-content: center; align-items: center; gap: 12px;
  }
  .back-lockup__square { width: 34px; height: 34px; background: #ffffff; }
  .back-lockup__name { color: #ffffff; font-weight: 800; font-size: 30px; letter-spacing: -0.5px; }
  .back-url {
    position: absolute; left: 0; right: 0; top: 262px; text-align: center;
    color: #ffffff; font-size: 13px; letter-spacing: 3px;
  }
</style>
</head>
<body>
<main class="card-sheet">
  <section class="card card--front" aria-label="Card front">
    <div class="brand-lockup">
      <div class="brand-square"></div>
      <div class="brand-name">
        <span class="brand-name__first">Marlowe</span>
        <span class="brand-name__second">Partners</span>
      </div>
    </div>
    <ul class="service-list">
      <li>Project Support</li>
      <li>Operations Analysis</li>
      <li>Business Development</li>
    </ul>
    <div class="contact-person">
      <p class="contact-person__name">Tom Brackett</p>
      <p class="contact-person__title">Solutions Strategist</p>
      <p>47 Pellham Road</p>
      <p>Suite K Boston, MA 02184</p>
    </div>
    <ul class="contact-lines">
      <li>
        <svg class="contact-icon" viewBox="0 0 14 14"><circle cx="7" cy="7" r="7" fill="var(--brand-blue)"/><path d="M4.5 3.5l1.5 0 .6 1.8-.9.7a5 5 0 0 0 2.3 2.3l.7-.9 1.8.6v1.5c-3.5.3-6.3-2.5-6-6z" fill="#fff"/></svg>
        617-555-0142
      </li>
      <li>
        <svg class="contact-icon" viewBox="0 0 14 14"><circle cx="7" cy="7" r="7" fill="var(--brand-blue)"/><path d="M4.5 3.5l1.5 0 .6 1.8-.9.7a5 5 0 0 0 2.3 2.3l.7-.9 1.8.6v1.5c-3.5.3-6.3-2.5-6-6z" fill="#fff"/></svg>
        508-555-0187
      </li>
      <li>
        <svg class="contact-icon" viewBox="0 0 14 14"><circle cx="7" cy="7" r="7" fill="var(--brand-blue)"/><rect x="3.5" y="4.5" width="7" height="5" fill="none" stroke="#fff" stroke-width="1"/><path d="M3.5 4.5l3.5 3 3.5-3" fill="none" stroke="#fff" stroke-width="1"/></svg>
        tbrackett@marlowepartners.example
      </li>
      <li>
        <svg class="contact-icon" viewBox="0 0 14 14"><circle cx="7" cy="7" r="7" fill="var(--brand-blue)"/><circle cx="7" cy="7" r="3.6" fill="none" stroke="#fff" stroke-width="1"/><path d="M3.4 7h7.2M7 3.4c-1.6 2-1.6 5.2 0 7.2M7 3.4c1.6 2 1.6 5.2 0 7.2" fill="none" stroke="#fff" stroke-width="0.8"/></svg>
        www.marlowepartners.example
      </li>
    </ul>
    <svg class="front-band" viewBox="0 0 540 40" preserveAspectRatio="none">
      <polygon points="0,14 300,14 318,40 0,40" fill="var(--brand-blue)"/>
      <polygon points="306,24 540,24 540,40 318,40" fill="var(--brand-blue-dark)"/>
    </svg>
  </section>

  <section class="card card--back" aria-label="Card back">
    <div class="back-lockup">
      <div class="back-lockup__square"></div>
      <span class="back-lockup__name">Marlowe Partners</span>
    </div>
    <p class="back-url">www.MarlowePartners.example</p>
  </section>
</main>
</body>
</html>
```